Doctors Office Web Design

Name of the business is Lin-Yue Hart M.D.
We need a web design that is attractive for women that want to see Dr. Lin-Yue Hart for Obstetrician Gynecology and Pregnancy care. Dr. Hart earned her degree from Carrow Ridge Medical College of obstetrician gynecology. We want to attract women of child bearing ages to come to our offices for health, education, and pregnancies.

Please visit http://www.drhartclinicweb.com/ to help you get a feel for who we are. We will be adding some pictures and logo in the next few days.

We are looking for to have pages for and tabs including
About Us- History, Our Staff, Dr. Hart
Patient Information- Appointments, E-Prescriptions, Payments Accepted, Insurance
Health- General, Sexual, Mental, Affiliates
Pregnancy- Minimally invasive surgery(our specialty), 4-D Ultra Sound, Hospital Affiliations
Media- News,Pictures, Videos
Locations- Palmer Office, Westvale Office

The colors we would like to use are pastel colors, magenta, and plum

Target Market(s)

Women of all ages with an emphasis on 25-65 year olds

Industry/Entity Type

Business

Requirements
Must have
• Needs to include a location for a our videos and pictures that I will submit shortly. We also want a map to our location or atleast a place for one.
Nice to have
• A place for a google map of our office locations.

```html
<!DOCTYPE html>
<html lang="en">
<head>
<meta charset="utf-8">
<title>Lin-Yue Hart M.D.</title>
<link rel="stylesheet" href="https://fonts.googleapis.com/css2?family=Ubuntu:wght@400;500;700&family=PT+Sans:wght@400;700&display=swap">
<style>
:root{
  --magenta:#c8167f;
  --magenta-bright:#e0218a;
  --plum:#8a1668;
  --plum-dark:#6e1253;
  --pastel:#fdeef6;
  --pastel-border:#f2cfe2;
  --ink:#4a4a4a;
  --ink-soft:#5c5c5c;
  --rule:#dddddd;
  --white:#ffffff;
}
*{box-sizing:border-box;margin:0;padding:0}
html,body{width:1050px;height:1200px;overflow:hidden}
body{position:relative;background:var(--white);font-family:"PT Sans",sans-serif;color:var(--ink)}
.abs{position:absolute}
.header-band{left:0;top:0;width:1050px;height:230px;background:linear-gradient(#e3e3e3,#f3f3f3);border-top:2px solid var(--magenta-bright)}
.footer-band{left:0;top:923px;width:1050px;height:277px;background:linear-gradient(var(--magenta-bright),#b01f7c 40%,#8a1f69)}
.util-tab{left:792px;top:0;width:166px;height:24px;background:var(--magenta-bright);border-radius:0 0 8px 8px;color:var(--white);font:12px "PT Sans",sans-serif;display:flex;align-items:center;justify-content:center;gap:6px}
.brand{left:108px;top:28px;font:500 27px "Ubuntu",sans-serif;letter-spacing:-.5px;color:var(--plum)}
.brand span{color:var(--ink-soft)}
.search{left:795px;top:32px;width:162px;height:23px;display:flex}
.search-field{flex:1;border:1px solid #d6d6d6;border-radius:12px 0 0 12px;background:var(--white);font:11px "PT Sans",sans-serif;color:#aaa;padding:5px 12px}
.search-go{width:35px;background:var(--plum);color:var(--white);border-radius:0 12px 12px 0;font:11px "PT Sans",sans-serif;display:flex;align-items:center;justify-content:center}
.main-nav{left:111px;top:92px;display:flex;gap:4px}
.main-nav a{height:27px;padding:0 8px;background:var(--plum);color:var(--white);font:500 12px "Ubuntu",sans-serif;border-radius:8px 8px 0 0;display:flex;align-items:center;text-decoration:none}
.follow{left:754px;top:92px;display:flex;align-items:center;gap:4px;font:16px "Ubuntu",sans-serif;color:#666}
.follow i{width:22px;height:22px;border-radius:3px;display:inline-block}
.hero{left:94px;top:118px;width:859px;height:293px;border-radius:10px;background:linear-gradient(135deg,#c3238d,#7e1260);overflow:hidden;border:3px solid var(--magenta)}
.hero-photo{position:absolute;left:0;top:0;width:562px;height:100%;background:linear-gradient(120deg,#d9d7d2,#eee8e2 45%,#c8cdd4)}
.hero-copy{position:absolute;left:573px;top:10px;width:270px;color:var(--white)}
.hero-copy h1{font:400 22px/26px "Ubuntu",sans-serif;letter-spacing:.5px;padding-bottom:10px;border-bottom:1px dotted rgba(255,255,255,.5)}
.hero-copy h1 b{font-weight:700;font-size:25px}
.hero-copy p{font:11px/17.5px "PT Sans",sans-serif;letter-spacing:.6px;margin-top:12px;text-align:justify}
.btn-light{display:inline-block;margin-top:14px;background:linear-gradient(#fff,#ddd);color:#777;font:500 14px "Ubuntu",sans-serif;padding:5px 14px;border-radius:14px}
.dots{position:absolute;left:706px;top:264px;display:flex;gap:11px}
.dots i{width:14px;height:14px;border-radius:50%;background:var(--magenta-bright)}
.dots i.on{border:3px solid var(--plum-dark)}
.content{left:94px;top:411px;width:859px;height:591px;background:var(--white);border-radius:0 0 10px 10px}
.feature{top:430px;width:193px}
.feature+.feature{}
.feature h2{display:flex;align-items:center;gap:6px;font:500 16px "Ubuntu",sans-serif;color:var(--ink);height:28px}
.feature h2 i{width:26px;height:26px;border-radius:50%;background:var(--pastel-border);display:inline-block}
.thumb{margin-top:8px;border:1px solid #ccc;padding:4px;height:72px}
.thumb div{width:100%;height:100%}
.feature p{font:10px/15.8px "PT Sans",sans-serif;color:var(--ink-soft);margin-top:12px;text-align:justify}
.feature ul{list-style:none;font:10px/15.8px "PT Sans",sans-serif;color:var(--ink-soft)}
.feature li{padding-left:14px;position:relative}
.feature li::before{content:"";position:absolute;left:4px;top:5px;border-left:4px solid var(--plum);border-top:3px solid transparent;border-bottom:3px solid transparent}
.pill{position:absolute;top:669px;font:10px "PT Sans",sans-serif;color:var(--white);background:var(--plum);padding:2px 7px;border-radius:8px}
.divider{top:430px;width:0;height:250px;border-left:1px dotted #ccc}
.office{left:96px;top:719px;width:562px;height:265px;background:var(--pastel);border:1px solid var(--pastel-border);border-radius:10px}
.map{position:absolute;left:11px;top:13px;width:316px;height:243px;background:var(--white);border:1px solid #ddd;border-radius:4px;padding:5px}
.map div{width:100%;height:100%;background:linear-gradient(135deg,#ede9e1,#f6f2ea 50%,#dfe9d6)}
.office h2{position:absolute;left:339px;top:21px;font:400 19px "Ubuntu",sans-serif;color:var(--ink)}
.office h2 span{color:var(--magenta)}
.office p{position:absolute;left:335px;top:56px;width:211px;font:10px/17.5px "PT Sans",sans-serif;color:var(--ink-soft);text-align:justify}
.btn-dark{position:absolute;left:458px;top:226px;background:#2f2f2f;color:var(--white);font:12px "PT Sans",sans-serif;padding:3px 10px;border-radius:10px}
.services{left:689px;top:720px;width:260px}
.services h2{font:500 18px "Ubuntu",sans-serif;color:var(--ink);letter-spacing:1px}
.services h2 span{color:var(--magenta)}
.services ul{list-style:none;margin-top:10px;font:10px/21px "PT Sans",sans-serif;color:var(--ink)}
.services li{padding-left:14px;position:relative}
.services li::before{content:"";position:absolute;left:2px;top:7px;border-left:4px solid var(--plum);border-top:3px solid transparent;border-bottom:3px solid transparent}
.footer h3{font:400 18px "Ubuntu",sans-serif;color:var(--white)}
.footer{color:var(--white)}
.foot-nav{left:115px;top:1014px}
.foot-nav ul{list-style:none;margin-top:8px;font:10.5px/14px "PT Sans",sans-serif;letter-spacing:.5px}
.foot-nav li{padding-left:13px;position:relative}
.foot-nav li::before{content:"";position:absolute;left:0;top:4px;border-left:4px solid var(--white);border-top:3px solid transparent;border-bottom:3px solid transparent}
.foot-rule{top:1025px;height:128px;border-left:1px dotted rgba(255,255,255,.45)}
.foot-hosp{left:274px;top:1014px;width:193px}
.foot-hosp p,.foot-contact p{font:10.5px/15.8px "PT Sans",sans-serif;letter-spacing:.6px;margin-top:8px;text-align:justify}
.foot-contact{left:514px;top:1021px}
.foot-contact .cols{display:flex;gap:26px}
.foot-contact p{text-align:left;margin-top:8px}
.badge{left:849px;top:1018px;width:96px;height:122px;background:var(--white)}
.badge div{margin:10px auto 0;width:52px;height:64px;border-radius:50%;background:linear-gradient(#d8c4e4,#a84e98)}
.copy{top:1180px;font:10.5px "PT Sans",sans-serif;letter-spacing:.4px;color:var(--white)}
</style>
</head>
<body>
<div class="abs header-band"></div>
<div class="abs footer-band"></div>

<nav class="abs util-tab"><span>Home</span>/<span>Register</span>/<span>Sitemap</span></nav>
<div class="abs brand">LIN-YUE HART <span>M.D.</span></div>
<div class="abs search"><div class="search-field">Search</div><div class="search-go">GO</div></div>

<nav class="abs main-nav">
  <a>About Us</a><a>Patient Information</a><a>Health</a><a>Pregnancy</a><a>Media</a><a>Locations</a>
</nav>
<div class="abs follow">Follow us on
  <i style="background:#3b5998" aria-label="Social profile"></i>
  <i style="background:#2aa9e0" aria-label="Social profile"></i>
  <i style="background:#1b7bb7" aria-label="Social profile"></i>
  <i style="background:#f08a24" aria-label="News feed"></i>
</div>

<section class="abs hero">
  <div class="hero-photo" role="img" aria-label="Photo of Dr. Hart greeting a smiling patient in the exam room"></div>
  <div class="hero-copy">
    <h1>Serving All Areas of<br><b>Women's Health,</b><br>Including:</h1>
    <p>Welcome to Dr. Lin-Yue Hart's website. Here you will be able to find information about both of our offices, meet Dr. Hart and her staff, and browse through our women's health links to learn more about pregnancy, nutrition, exercise, and other women's health issues.</p>
    <span class="btn-light">More info</span>
  </div>
  <div class="dots"><i></i><i></i><i></i><i></i><i class="on"></i><i></i></div>
</section>

<div class="abs content"></div>

<article class="abs feature" style="left:103px">
  <h2><i></i>About the Practice</h2>
  <div class="thumb"><div role="img" aria-label="Photo of the practice staff" style="background:linear-gradient(#e8c76a,#c9a6b8)"></div></div>
  <p>All about Lin-Yue Hart, M.D., P.A. Includes addresses, directions, contact numbers, office hours,<br><br>Dr. Hart's hospital affiliations, and insurance plans accepted.Dr. Hart's hospital affiliations, and insurance</p>
</article>
<span class="pill" style="left:230px">more info</span>
<div class="abs divider" style="left:307px"></div>

<article class="abs feature" style="left:316px">
  <h2><i></i>Meet Dr. Hart</h2>
  <div class="thumb"><div role="img" aria-label="Portrait photo of Dr. Hart" style="background:linear-gradient(#d9d9d9,#9a9a9a)"></div></div>
  <p>Dr. Hart's goal is to provide current and compassionate women's healthcare in a fashion that acknowledges her patients' diverse values, backgrounds, and conditions. Dr. Hart acknowledges the whole individual and recognizes the inseparability of the body.</p>
</article>
<span class="pill" style="left:449px">more info</span>
<div class="abs divider" style="left:522px"></div>

<article class="abs feature" style="left:534px">
  <h2><i></i>Women's Health Info</h2>
  <div class="thumb"><div role="img" aria-label="Photo of the office reception desk" style="background:linear-gradient(#e4e1da,#a6a08e)"></div></div>
  <p>(GYN) Get answers to your gynecologic and women's health concerns by following links to academic articles, medical sites, and to special.<br><br>medical sites, and to special information that Dr. Hart provides to her patients.</p>
</article>
<span class="pill" style="left:668px">more info</span>
<div class="abs divider" style="left:737px"></div>

<article class="abs feature" style="left:750px">
  <h2><i></i>The Pregnancy</h2>
  <div class="thumb"><div role="img" aria-label="Photo of the care team" style="background:linear-gradient(#d8dbe3,#e8b27a)"></div></div>
  <p style="margin-bottom:0">Where can I find more information about</p>
  <ul><li>pregnancy?</li><li>Preconceptional Care</li><li>Pregnancy Testing</li><li>Pregnancy Health</li><li>High Risk Pregnancy</li><li>Pregnancy Loss</li></ul>
</article>
<span class="pill" style="left:888px">more info</span>

<section class="abs office">
  <div class="map"><div role="img" aria-label="Street map showing the office location"></div></div>
  <h2>Office<span>Location</span></h2>
  <p>Dr. Hart serves her patients in two different offices. On Mondays, Tuesdays and Thursdays, Dr. Hart sees patients in her Westvale office, and on Wednesdays and Fridays, she sees patients in Palmer. Please call either number for an appointment. Pharmacies can also fax requests via Dr. Hart's fax number at her Westvale office.</p>
  <span class="btn-dark">View Full Map</span>
</section>

<section class="abs services">
  <h2>Serv<span>ices</span></h2>
  <ul>
    <li>How do I find general information on women's health?</li>
    <li>What can I find information on living healthily?</li>
    <li>Where can I find answers to questions?</li>
    <li>What is Acupuncture? Where can I find more?</li>
    <li>Just for Fun</li>
    <li>How do I find general information on women's health?</li>
    <li>What can I find information on living healthily?</li>
    <li>Where can I find answers to questions?</li>
    <li>What is Acupuncture? Where can I find more?</li>
    <li>Just for Fun</li>
  </ul>
</section>
<span class="pill" style="left:868px;top:975px">more info</span>

<footer class="footer">
  <div class="abs foot-nav">
    <h3>Navigate</h3>
    <ul><li>Home</li><li>About Us</li><li>Patient Information</li><li>Health</li><li>Pregnancy</li><li>Media</li><li>Locations</li></ul>
  </div>
  <div class="abs foot-rule" style="left:258px"></div>
  <div class="abs foot-hosp">
    <h3>Hospital Affiliations</h3>
    <p>Dr. Hart is a member of the medical staffs of Linden Memorial Hospital and Palmer Community Hospital. She is a member of the medical team at the Linden Health Women's Health Center.</p>
  </div>
  <div class="abs foot-rule" style="left:487px"></div>
  <div class="abs foot-contact">
    <h3>Contact us</h3>
    <div class="cols">
      <p>2240 Orchard Lane Avenue<br>Suite 115-116<br>Westvale, Florida 40112<br>Tel: (555) 201-4545<br>Fax: (555) 201-0528</p>
      <p>870 N.W. 9th Street<br>Suite 110A<br>Palmer, Florida 40118<br>Tel: (555) 318-4014<br>Fax: (555) 318-2753</p>
    </div>
  </div>
  <div class="abs badge" role="img" aria-label="Awareness month badge"><div></div></div>
  <div class="abs copy" style="left:113px">(c) Copyright 2002, Lin-Yue Hart, M.D., P.A, Website Powerd by Brightpane.</div>
  <div class="abs copy" style="left:816px">© 2011 The Doctors of Westvale</div>
</footer>
</body>
</html>
```